Booklet Cover Design Project

Booklet cover designs - I have uploaded a couple of examples of previous covers - they should match these in concept!.

4 covers using the same theme :

1
Work Health and Safety (Medical)
QNVLMX528

2. Maintain Patient Records
QNVRTA614

3. Prepare and Process Medical Accounts
QNVRTA619

4. Confidentiality, Privacy and Security in a Medical Office
QNVRTA687

** I have uploaded a couple of samples from previous work - please use a similar style for consistency. Suggested photo samples attached.

Requirements
Must have
• Consistency of theme

```html
<!DOCTYPE html>
<html lang="en">
<head>
<meta charset="utf-8">
<title>Medical Administration Booklet Covers</title>
<link rel="stylesheet" href="https://fonts.googleapis.com/css2?family=Cinzel:wght@400;600;700&display=swap">
<style>
  :root {
    --navy: #1b2b56;
    --gold: #f2c25c;
    --paper: #ffffff;
    --backdrop: #ecedf0;
    --author: #2d3a5c;
  }
  * { box-sizing: border-box; margin: 0; padding: 0; }
  html, body {
    width: 1200px; height: 488px; overflow: hidden;
    background: var(--backdrop);
    font-family: "Cinzel", serif;
    color: var(--navy);
  }
  .cover-row { position: relative; width: 1200px; height: 488px; }
  .cover {
    position: absolute; top: 59px;
    width: 263px; height: 370px;
    background: var(--paper);
    box-shadow: 0 2px 8px rgba(20, 30, 60, .18);
    overflow: hidden;
  }
  .cover--health { left: 41px; }
  .cover--records { left: 324px; }
  .cover--accounts { left: 608px; }
  .cover--privacy { left: 891px; }

  .brand {
    position: absolute; top: 11px; left: 0; width: 100%;
    text-align: center; line-height: 1.05;
  }
  .brand__name { font-size: 4px; font-weight: 600; letter-spacing: .1px; display: block; }
  .brand__mark {
    display: block; width: 22px; height: 22px; margin: 2px auto 2px;
    border-radius: 50%; background: var(--navy);
  }
  .brand__tagline { font-size: 2.6px; letter-spacing: .1px; display: block; }

  .title { position: absolute; inset: 0; font-weight: 600; }
  .title span { position: absolute; line-height: 1; white-space: nowrap; }
  .title .initial { font-weight: 400; }
  .title small { font-size: 5.5px; font-weight: 400; }

  .code-band {
    position: absolute; top: 134px; left: 0; width: 100%; height: 5px;
    background: var(--navy);
  }
  .code-pill {
    position: absolute; top: 128px; left: 50%; transform: translateX(-50%);
    width: 86px; height: 19px; border-radius: 9px;
    background: var(--navy); color: var(--gold);
    font-size: 9px; font-weight: 700; letter-spacing: .2px;
    display: flex; align-items: center; justify-content: center;
  }

  .cover-photo { position: absolute; top: 153px; left: 0; width: 100%; height: 156px; }
  .cover--health .cover-photo { background: linear-gradient(120deg, #3f9be0 0%, #cfe4f3 28%, #f1f3f5 60%, #dfe3e7 100%); }
  .cover--records .cover-photo { background: linear-gradient(110deg, #6a4a36 0%, #b98e73 35%, #ecebe8 60%, #c8c3bf 100%); }
  .cover--accounts .cover-photo { background: linear-gradient(130deg, #f4f7fb 0%, #dce9f4 45%, #a9c4dc 80%, #5a7590 100%); }
  .cover--privacy .cover-photo { background: linear-gradient(120deg, #2c4e95 0%, #3b6cc4 50%, #1f3b72 100%); }

  .author {
    position: absolute; top: 322px; left: 0; width: 100%;
    text-align: center; font-size: 9px; letter-spacing: 5px;
    color: var(--author); font-weight: 400;
  }
</style>
</head>
<body>
<main class="cover-row">

  <article class="cover cover--health">
    <div class="brand"><span class="brand__name">ARDENVALE INSTITUTE<br>OF TRAINING</span><span class="brand__mark"></span><span class="brand__tagline">Building Skills | Growing Careers</span></div>
    <h1 class="title">
      <span class="initial" style="left:41px;top:56px;font-size:60px">H</span>
      <span style="left:94px;top:59px;font-size:17px">WORK</span>
      <span style="left:95px;top:77px;font-size:29px">EALTH</span>
      <span style="left:81px;top:107px;font-size:17px">AND SAFETY<small> (MEDICAL)</small></span>
    </h1>
    <div class="code-band"></div>
    <div class="code-pill">QNVLMX528</div>
    <div class="cover-photo" role="img" aria-label="Photo of blue medical gloves, a surgical mask and safety glasses"></div>
    <p class="author">AUTHOR NAME</p>
  </article>

  <article class="cover cover--records">
    <div class="brand"><span class="brand__name">ARDENVALE INSTITUTE<br>OF TRAINING</span><span class="brand__mark"></span><span class="brand__tagline">Building Skills | Growing Careers</span></div>
    <h1 class="title">
      <span class="initial" style="left:56px;top:53px;font-size:56px">P</span>
      <span style="left:89px;top:57px;font-size:13px;letter-spacing:-.3px">MAINTAIN</span>
      <span style="left:88px;top:73px;font-size:32px">ATIENT</span>
      <span style="right:55px;top:101px;font-size:15px">RECORD</span>
    </h1>
    <div class="code-band"></div>
    <div class="code-pill">QNVRTA614</div>
    <div class="cover-photo" role="img" aria-label="Photo of a staff member searching colour-coded patient files on a shelf"></div>
    <p class="author">AUTHOR NAME</p>
  </article>

  <article class="cover cover--accounts">
    <div class="brand"><span class="brand__name">ARDENVALE INSTITUTE<br>OF TRAINING</span><span class="brand__mark"></span><span class="brand__tagline">Building Skills | Growing Careers</span></div>
    <h1 class="title">
      <span class="initial" style="left:43px;top:49px;font-size:54px">M</span>
      <span style="left:101px;top:60px;font-size:8.5px;letter-spacing:-.2px">PREPARE &amp; PROCESS</span>
      <span style="left:102px;top:70px;font-size:33px">EDICAL</span>
      <span style="right:42px;top:98px;font-size:15px">ACCOUNTS</span>
    </h1>
    <div class="code-band"></div>
    <div class="code-pill">QNVRTA619</div>
    <div class="cover-photo" role="img" aria-label="Photo of a doctor using a calculator beside a laptop with medical icons overlaid"></div>
    <p class="author">AUTHOR NAME</p>
  </article>

  <article class="cover cover--privacy">
    <div class="brand"><span class="brand__name">ARDENVALE INSTITUTE<br>OF TRAINING</span><span class="brand__mark"></span><span class="brand__tagline">Building Skills | Growing Careers</span></div>
    <h1 class="title">
      <span class="initial" style="left:36px;top:55px;font-size:50px">M</span>
      <span style="left:94px;top:56px;font-size:9.5px">CONFIDENTIALITY</span>
      <span style="left:94px;top:67px;font-size:9.5px">PRIVACY &amp; SECURITY<small> IN A</small></span>
      <span style="left:96px;top:78px;font-size:32px">EDICAL</span>
      <span style="right:35px;top:103px;font-size:16px">OFFICE</span>
    </h1>
    <div class="code-band"></div>
    <div class="code-pill">QNVRTA687</div>
    <div class="cover-photo" role="img" aria-label="Photo of a medical worker holding a red heart with a padlock amid healthcare icons"></div>
    <p class="author">AUTHOR NAME</p>
  </article>

</main>
</body>
</html>
```